Safety Work Area Signage to keep people away from work zone

We would like to create a simple design that will include our logo and phone number, 'work area', and 'caution / cuidado' (please see a mock-up of the intended design in the uploaded files). Please provide multiple options. We would like a Professional look for the poster as it is meant for safety. Poster Size to be: 18.16" X 23.10"

Target Market(s)

General Public on Construction Sites

Font styles to use
Serif

Requirements
Must have
• see mock-ups in uploaded files
Nice to have
• Simple Design, Professional Look

```html
<!DOCTYPE html>
<html lang="en">
<head>
<meta charset="utf-8">
<title>Work Area Safety Sign Options</title>
<link rel="stylesheet" href="https://fonts.googleapis.com/css2?family=Arimo:wght@700&family=Source+Serif+4:opsz,wght@8..60,700&display=swap">
<style>
  :root {
    --backdrop: #5e5e5e;
    --safety-yellow: #fde32a;
    --sign-black: #262626;
    --panel-white: #ffffff;
  }
  html, body {
    margin: 0;
    padding: 0;
    width: 1200px;
    height: 878px;
    overflow: hidden;
    background: var(--backdrop);
  }
  .board {
    position: relative;
    width: 1200px;
    height: 878px;
  }
  .sign {
    position: absolute;
    top: 113px;
    width: 512px;
    height: 652px;
    filter: drop-shadow(0 3px 4px rgba(0,0,0,0.35));
  }
  .sign--light { left: 59px; }
  .sign--dark { left: 627px; }
  .sans { font-family: "Arimo", Arial, sans-serif; font-weight: 700; }
  .serif { font-family: "Source Serif 4", Georgia, serif; font-weight: 700; }
  .fill-yellow { fill: var(--safety-yellow); }
  .fill-black { fill: var(--sign-black); }
  .fill-white { fill: var(--panel-white); }
  .sign--light .brand-ink { fill: var(--sign-black); }
  .sign--dark .brand-ink { fill: var(--safety-yellow); }
  .sign--light .brand-rule { stroke: var(--sign-black); }
  .sign--dark .brand-rule { stroke: var(--safety-yellow); }
  .sign--light .alert-ink { fill: var(--panel-white); }
  .sign--dark .alert-ink { fill: var(--safety-yellow); }
</style>
</head>
<body>
<main class="board">

  <svg class="sign sign--light" viewBox="0 0 512 652" aria-label="Caution work area sign, white company panel">
    <defs>
      <pattern id="hazard-light" width="26" height="14" patternUnits="userSpaceOnUse">
        <polygon class="fill-black" points="10,0 26,0 16,14 0,14"/>
      </pattern>
    </defs>
    <rect class="fill-yellow" x="0" y="0" width="512" height="652"/>
    <g transform="translate(0 10)"><rect fill="url(#hazard-light)" x="0" y="0" width="512" height="14"/></g>
    <rect class="fill-black" x="0" y="31" width="512" height="97"/>
    <g class="alert-icon">
      <path class="alert-ink" d="M68,47 Q72,41 76,47 L108,103 Q112,111 104,111 L40,111 Q32,111 36,103 Z"/>
      <rect class="fill-black" x="67" y="66" width="10" height="27"/>
      <rect class="fill-black" x="67" y="96" width="10" height="8"/>
    </g>
    <text class="sans alert-ink" x="131" y="107" font-size="67" textLength="329" lengthAdjust="spacingAndGlyphs">CAUTION</text>
    <g transform="translate(0 136)"><rect fill="url(#hazard-light)" x="0" y="0" width="512" height="14"/></g>
    <text class="sans fill-black" x="256" y="241" font-size="100" text-anchor="middle" textLength="322" lengthAdjust="spacingAndGlyphs">WORK</text>
    <text class="sans fill-black" x="256" y="330" font-size="100" text-anchor="middle" textLength="295" lengthAdjust="spacingAndGlyphs">AREA</text>
    <rect class="fill-black" x="0" y="361" width="512" height="138"/>
    <rect class="fill-white" x="0" y="365" width="512" height="129"/>
    <g class="brand-lockup">
      <text class="serif brand-ink" x="140" y="406" font-size="38" text-anchor="middle">Harlow &amp;</text>
      <text class="serif brand-ink" x="140" y="434" font-size="21" text-anchor="middle">Company, Inc.</text>
      <line class="brand-rule" x1="247" y1="376" x2="247" y2="443" stroke-width="2"/>
      <text class="serif brand-ink" x="357" y="404" font-size="32" text-anchor="middle">General</text>
      <text class="serif brand-ink" x="357" y="433" font-size="32" text-anchor="middle">Contractors</text>
      <text class="serif brand-ink" x="257" y="474" font-size="28" text-anchor="middle">“We Build Lasting Trust”®</text>
    </g>
    <text class="sans fill-black" x="256" y="541" font-size="39" text-anchor="middle" textLength="294" lengthAdjust="spacingAndGlyphs">(555) 214-0387</text>
    <text class="sans fill-black" x="256" y="621" font-size="83" text-anchor="middle" textLength="433" lengthAdjust="spacingAndGlyphs">CUADADO</text>
    <g transform="translate(0 638)"><rect fill="url(#hazard-light)" x="0" y="0" width="512" height="14"/></g>
  </svg>

  <svg class="sign sign--dark" viewBox="0 0 512 652" aria-label="Caution work area sign, black company panel">
    <defs>
      <pattern id="hazard-dark" width="26" height="14" patternUnits="userSpaceOnUse">
        <polygon class="fill-black" points="10,0 26,0 16,14 0,14"/>
      </pattern>
    </defs>
    <rect class="fill-yellow" x="0" y="0" width="512" height="652"/>
    <g transform="translate(0 10)"><rect fill="url(#hazard-dark)" x="0" y="0" width="512" height="14"/></g>
    <rect class="fill-black" x="0" y="31" width="512" height="97"/>
    <g class="alert-icon">
      <path class="alert-ink" d="M68,47 Q72,41 76,47 L108,103 Q112,111 104,111 L40,111 Q32,111 36,103 Z"/>
      <rect class="fill-black" x="67" y="66" width="10" height="27"/>
      <rect class="fill-black" x="67" y="96" width="10" height="8"/>
    </g>
    <text class="sans alert-ink" x="131" y="107" font-size="67" textLength="329" lengthAdjust="spacingAndGlyphs">CAUTION</text>
    <g transform="translate(0 136)"><rect fill="url(#hazard-dark)" x="0" y="0" width="512" height="14"/></g>
    <text class="sans fill-black" x="256" y="241" font-size="100" text-anchor="middle" textLength="322" lengthAdjust="spacingAndGlyphs">WORK</text>
    <text class="sans fill-black" x="256" y="330" font-size="100" text-anchor="middle" textLength="295" lengthAdjust="spacingAndGlyphs">AREA</text>
    <rect class="fill-black" x="0" y="365" width="512" height="129"/>
    <g class="brand-lockup">
      <text class="serif brand-ink" x="140" y="406" font-size="38" text-anchor="middle">Harlow &amp;</text>
      <text class="serif brand-ink" x="140" y="434" font-size="21" text-anchor="middle">Company, Inc.</text>
      <line class="brand-rule" x1="247" y1="376" x2="247" y2="443" stroke-width="2"/>
      <text class="serif brand-ink" x="357" y="404" font-size="32" text-anchor="middle">General</text>
      <text class="serif brand-ink" x="357" y="433" font-size="32" text-anchor="middle">Contractors</text>
      <text class="serif brand-ink" x="257" y="474" font-size="28" text-anchor="middle">“We Build Lasting Trust”®</text>
    </g>
    <text class="sans fill-black" x="256" y="541" font-size="39" text-anchor="middle" textLength="294" lengthAdjust="spacingAndGlyphs">(555) 214-0387</text>
    <text class="sans fill-black" x="256" y="621" font-size="83" text-anchor="middle" textLength="433" lengthAdjust="spacingAndGlyphs">CUADADO</text>
    <g transform="translate(0 638)"><rect fill="url(#hazard-dark)" x="0" y="0" width="512" height="14"/></g>
  </svg>

</main>
</body>
</html>
```